Business card design needed

A Moth's Fern

I would like a design for a small business specializing in earrings made from Tasmanian timber combined with coloured beads. I see the brand as a modern take on wooden earrings, fun and beautiful with the wood being laser cut Tasmanian timber combined with a coloured sometimes metallic bead.

I see the logo design as a little cute, perhaps a ladybug on a leaf and would like a combination of green and white. I have seen a quirky take on the traditional red ladybug done in pink with black spots on a green leaf that I like but I'm very open to ideas and suggestions.

Target Market(s)

Women primarily aged 20-50

Industry/Entity Type

Small Business

Contact Information for Business Card

A Moth's Fern
Tasmanian Timber & Beaded Design Earrings

www.pagebook.example/amothsfern
www.craftnook.example/amothsfern

Logo Text

A Moth's Fern

Requirements
Must have
• Must have some white on the business card. The cards are being matched with Tasmanian Timber earrings so whites and greens with a splash of colour is okay, but nothing to crazy or bright.

```html
<!DOCTYPE html>
<html lang="en">
<head>
<meta charset="utf-8">
<title>A Moth's Fern — Business Card</title>
<link href="https://fonts.googleapis.com/css2?family=Schoolbell&family=Arimo:wght@400&display=swap" rel="stylesheet">
<style>
  :root {
    --page: #ffffff;
    --card: #ffffff;
    --card-shadow: rgba(0, 0, 0, 0.22);
    --leaf-light: #d9e46a;
    --leaf-mid: #b5c93c;
    --leaf-deep: #8fa82a;
    --bug-pink: #e23f8f;
    --bug-soft: #f28cbc;
    --ink: #3a3a3a;
    --ink-body: #2e2e2e;
    --accent: #c8177e;
  }
  * { margin: 0; padding: 0; box-sizing: border-box; }
  html, body {
    width: 1200px;
    height: 799px;
    overflow: hidden;
    background: var(--page);
  }
  .canvas {
    position: relative;
    width: 1200px;
    height: 799px;
  }
  .business-card {
    position: absolute;
    left: 104px;
    top: 104px;
    width: 1017px;
    height: 552px;
    background: var(--card);
    box-shadow: 1px 3px 4px var(--card-shadow);
    overflow: hidden;
  }
  .leaf-photo {
    position: absolute;
    left: 0;
    top: 0;
    width: 470px;
    height: 552px;
  }
  .ladybug-illustration {
    position: absolute;
    left: 782px;
    top: 58px;
    width: 170px;
    height: 130px;
  }
  .card-copy {
    position: absolute;
    right: 104px;
    top: 246px;
    text-align: right;
  }
  .copy-heading {
    font-family: "Schoolbell", cursive;
    font-size: 41px;
    font-weight: 400;
    color: var(--ink);
    line-height: 1;
    margin-bottom: 16px;
  }
  .copy-materials {
    font-family: "Arimo", Arial, sans-serif;
    font-size: 23px;
    color: var(--ink-body);
    line-height: 35px;
  }
  .shop-link {
    display: block;
    font-family: "Arimo", Arial, sans-serif;
    font-size: 27px;
    color: var(--accent);
    margin-top: 52px;
    letter-spacing: 0.2px;
  }
</style>
</head>
<body>
<main class="canvas">
  <section class="business-card" aria-label="A Moth's Fern business card">
    <svg class="leaf-photo" viewBox="0 0 470 552" role="img" aria-label="Photograph of a bright green leaf with fine veins, sweeping in from the left edge">
      <defs>
        <linearGradient id="leafTone" x1="0" y1="0" x2="1" y2="1">
          <stop offset="0" stop-color="var(--leaf-light)"/>
          <stop offset="0.55" stop-color="var(--leaf-mid)"/>
          <stop offset="1" stop-color="var(--leaf-deep)"/>
        </linearGradient>
      </defs>
      <path d="M0 0 H462 C470 120 440 250 380 340 C320 430 220 500 110 552 H0 Z" fill="url(#leafTone)"/>
    </svg>

    <svg class="ladybug-illustration" viewBox="0 0 170 130" role="img" aria-label="Illustration of a pink ladybug with black spots and curly antennae">
      <defs>
        <radialGradient id="bugTone" cx="0.55" cy="0.5" r="0.55">
          <stop offset="0" stop-color="var(--bug-pink)"/>
          <stop offset="1" stop-color="var(--bug-soft)"/>
        </radialGradient>
      </defs>
      <ellipse cx="100" cy="78" rx="50" ry="40" fill="url(#bugTone)"/>
    </svg>

    <div class="card-copy">
      <h1 class="copy-heading">Earrings made of:</h1>
      <p class="copy-materials">Laser-cut Tasmanian Timber and<br>Colorful, beautiful and fun beads</p>
      <span class="shop-link">www.craftnook.example/amothsfern</span>
    </div>
  </section>
</main>
</body>
</html>
```